Innovative Consulting Firm Needs New Business Cards and Stationary

Our Innovative Consulting Firm, Larkfield Consulting, is in need of new business cards and stationary designs. We want two-sided cards that incorporate our logo, which is attached. We are looking for something not too formal, but is professional and slick.

Card should have the following information:
Name (ex. Tom Bradley)
Title (ex. Manager)
Address (ex. 24680 Cedar Lane)
Address 2 (ex. Suite 100)
City
State
Zip Code
Mobile
Email

The card should also have our website: www.larkfieldconsulting.example

Industry/Entity Type

Management Consulting

Contact Information for Business Card

Name (ex. Tom Bradley)
Title (ex. Manager)
Address 2 (ex. Suite 100)
City
State
Zip Code
Mobile
Email

Font styles to use
Sans Serif

Requirements
Must have
• The colors on the card must match the colors in the logo. The exact color codes are attached in a pdf.
Nice to have
• The Company's Tagline is "Focused on your Future". This might be nice to incorporate, but not necessary.

```html
<!DOCTYPE html>
<html lang="en">
<head>
<meta charset="UTF-8">
<title>Larkfield Consulting — Business Card</title>
<link rel="stylesheet" href="https://fonts.googleapis.com/css2?family=Montserrat:wght@600&family=Roboto:wght@400;700&display=swap">
<style>
  :root {
    --blue: #2b5c8f;
    --blue-dark: #1c4270;
    --blue-deep: #163660;
    --orange: #f6a800;
    --silver: #d2d4d6;
    --silver-dark: #a9adb1;
    --paper: #f4f4f4;
    --white: #ffffff;
    --ink: #1e4b7c;
  }
  * { margin: 0; padding: 0; box-sizing: border-box; }
  html, body {
    width: 1200px; height: 720px; overflow: hidden;
    background: var(--white);
  }
  .card {
    position: relative;
    width: 1200px; height: 720px;
    overflow: hidden;
    background: linear-gradient(180deg, var(--blue) 0%, var(--blue-dark) 100%);
    font-family: "Roboto", Arial, sans-serif;
    color: var(--white);
  }
  .brand-panel {
    position: absolute; left: 0; top: 30px; width: 1200px; height: 270px;
    background: linear-gradient(180deg, var(--white) 0%, var(--paper) 60%, #e6e7e8 100%);
    border-top: 4px solid var(--silver-dark);
    border-bottom: 4px solid var(--silver-dark);
  }
  .brand-name {
    position: absolute; left: 0; right: 0; top: 52px;
    text-align: center;
    font-family: "Montserrat", Arial, sans-serif;
    font-weight: 600;
    color: var(--ink);
  }
  .brand-name .word {
    display: block;
    font-size: 104px; line-height: 1;
    letter-spacing: 2px;
  }
  .brand-name .sub {
    display: block;
    margin-top: 10px;
    padding-left: 330px;
    font-size: 30px; letter-spacing: 9px;
  }
  .name-band {
    position: absolute; left: 0; top: 314px; width: 1200px; height: 58px;
    background: var(--orange);
    display: flex; align-items: center; justify-content: center;
    font-weight: 700; font-size: 36px; letter-spacing: 1px;
    color: var(--blue-dark);
  }
  .title-band {
    position: absolute; left: 0; top: 372px; width: 1200px; height: 34px;
    background: linear-gradient(180deg, var(--silver) 0%, #bfc2c5 100%);
    display: flex; align-items: center; justify-content: center;
    font-size: 20px; color: var(--blue-dark); letter-spacing: 0.5px;
  }
  .contact {
    position: absolute; top: 418px;
    font-style: normal;
    font-size: 26px; line-height: 33px; text-transform: uppercase;
  }
  .contact--left { left: 166px; }
  .contact--right { left: 704px; }
  .web-band {
    position: absolute; left: 0; top: 600px; width: 1200px; height: 46px;
    background: linear-gradient(180deg, #e2e3e4 0%, var(--silver) 50%, #b8bbbe 100%);
    display: flex; align-items: center; justify-content: center;
    font-size: 23px; letter-spacing: 1px; text-transform: uppercase;
    color: var(--blue-deep);
  }
  .base-band {
    position: absolute; left: 0; top: 646px; width: 1200px; height: 74px;
    background: linear-gradient(180deg, var(--blue) 0%, var(--blue-deep) 100%);
  }
</style>
</head>
<body>
  <main class="card">
    <section class="brand-panel">
      <div class="brand-name">
        <span class="word">Larkfield</span>
        <span class="sub">CONSULTING</span>
      </div>
    </section>

    <div class="name-band">NAME (EX. TOM BRADLEY)</div>
    <div class="title-band">TITLE (EX. MANAGER)</div>

    <address class="contact contact--left">
      Address<br>
      (Ex. 24680 Cedar Lane)<br>
      Address 2<br>
      (Ex. Suite 100)
    </address>
    <address class="contact contact--right">
      City<br>
      State<br>
      Zip Code<br>
      Mobile<br>
      Email
    </address>

    <div class="web-band">www.larkfieldconsulting.example</div>
    <div class="base-band"></div>
  </main>
</body>
</html>
```